Website for KiLa online school

I need to get a website for my new online school KiLa Solvander learning. This is a new online school in Norway, offering online courses for expats and other people taking courses in Norwegian and Social Studies, which is mandatory to get permanent residency in Norway. The company needs a simple and functional website that will attract students. It should be easy to use, easy to find information and it has to look professional. The website should have a clean design. simple pictures related to online studies, languages, international connections etc.

Important points:
- I want to use the domain www.solvanderlearn.no and www.solvanderlearn.com in one domain, so if you write www.solvanderlearn.com you will maybe end up in www.solvanderlearn.no/en or something. I own both domains.
- the following words have to be mentioned many times: online learning, norwegian studies, sarn, emt, approved by emt, approved by sarn, norwegian course, study online etc. I guess I will make the text myself? I would like to get some help to make the text in English.
- I want to also have a chatterloom page, but that can come later

I need the following:

- website in both Norwegian and English (customers can click the flag to get English or Norwegian text)
- payment solution with Corda/Bluvex AND coinlyx AND frensa AND invoice - so a payment solution that is easy to use
-clean design
-easy to use
-also adjusted to smartphones and tablets

Logo image is uploaded, but I am waiting for the original files form the designer of the logo. It will come on Monday.

website text added, but this is only a draft. can be used to illustrate

Expats and all people who want to study Norwegian online

Education

1 page

Serif
Sans Serif

fbee3e
e34197
0455a3
9bcb3c
00a990
a64599
333333
ffffff
9d9d9d

• - payment option for corda/bluvex/coinlyx/frensa and invoice. Most important is the corda and bluvex payment
• - two languages: norwegian and english
• - www.solvanderlearn.com should automatically be transeferred to www.solvanderlearn.no/en
• - simple and clean design
• -have to look professional and serious, although colors are used
• pictures related to learning and online studies, as well as language and internatinal relations
• norwegian flags
• too many colors
• too much details

```html
<!DOCTYPE html>
<html lang="en">
<head>
<meta charset="utf-8">
<title>KiLa Solvander learning – Online Norwegian Studies</title>
<link href="https://fonts.googleapis.com/css2?family=Della+Respira&family=Roboto:wght@300;400;500;700&display=swap" rel="stylesheet">
<style>
:root{
  --orange:#f29a1f;
  --orange-dark:#e08a12;
  --teal:#1c8f96;
  --teal-light:#2aa3a6;
  --green:#7cb83e;
  --magenta:#e0197a;
  --ink:#333333;
  --dark:#2e2e2e;
  --darker:#262626;
  --grey:#9d9d9d;
  --light:#f4f4f4;
  --white:#ffffff;
  --serif:'Della Respira', Georgia, serif;
  --sans:'Roboto', Arial, sans-serif;
}
*{margin:0;padding:0;box-sizing:border-box}
html,body{width:1200px;height:4478px;overflow:hidden}
body{position:relative;font-family:var(--sans);color:var(--ink);background:var(--white)}
.section{position:absolute;left:0;width:1200px;overflow:hidden}
.abs{position:absolute}
.photo{position:absolute}

/* header / hero */
.hero{top:0;height:710px;background:linear-gradient(180deg,#cfcfcf 0%,#a9a9a9 45%,#8d8d8d 100%)}
.hero-photo{left:0;top:0;width:1200px;height:710px;background:linear-gradient(90deg,#bdbdbd 0%,#c8c8c8 40%,#b5b5b5 60%,#9a9a9a 100%)}
.hero-person{left:560px;top:150px;width:330px;height:560px;background:linear-gradient(180deg,#5a3f30 0%,#c94a55 45%,#d9d9d9 75%,#9a9a9a 100%);border-radius:160px 160px 0 0;opacity:.85}
.social{top:0;left:81px;display:flex;gap:4px}
.social span{display:block;width:36px;height:44px;background:#4a4a4a;color:var(--white);font-size:9px;line-height:44px;text-align:center}
.social span.on{background:var(--orange)}
.flag{top:0;left:1068px;width:54px;height:51px;background:linear-gradient(135deg,#1f3f8c 0%,#ffffff 50%,#c8202e 100%)}
.brand{display:flex;align-items:center;gap:14px}
.brand i{display:block;width:58px;height:58px;border-radius:50%;background:var(--orange)}
.brand b{font-family:var(--sans);font-weight:400;color:var(--white);display:block;font-size:48px;line-height:1}
.brand small{font-family:var(--sans);font-weight:400;color:var(--white);font-size:13px;display:block;margin-top:2px}
.hero .brand{top:62px;left:80px}
.nav{top:94px;left:440px;display:flex;gap:34px;font-size:15px;color:var(--white)}
.nav a{color:var(--white);text-decoration:none;padding-bottom:6px}
.nav a.active{border-bottom:2px solid var(--white)}
.login{top:82px;left:985px;width:137px;height:52px;background:var(--orange);color:var(--ink);font-size:16px;display:flex;align-items:center;justify-content:center}
.hero-title{top:308px;left:80px;color:var(--white);font-weight:700;font-size:34px;line-height:38px;letter-spacing:1px;text-transform:uppercase;padding-bottom:10px;border-bottom:2px solid rgba(255,255,255,.6);width:460px}
.hero-sub{top:400px;left:80px;width:460px;color:var(--white);font-size:28px;line-height:32px;font-weight:300}
.arrows{top:513px;left:80px;display:flex;gap:18px}
.arrows span{width:48px;height:48px;background:#1e1e1e;color:var(--white);font-size:22px;display:flex;align-items:center;justify-content:center;font-weight:700}

/* welcome */
.welcome{top:710px;height:341px;background:var(--white)}
.welcome-photo{left:60px;top:20px;width:270px;height:321px;background:linear-gradient(180deg,#efe3d2 0%,#d9c3a4 40%,#3c3c3c 100%);border-radius:130px 130px 0 0;filter:grayscale(1)}
.welcome h2{position:absolute;top:50px;left:510px;font-family:var(--serif);font-weight:400;color:var(--orange);font-size:50px;display:flex;align-items:center;gap:18px}
.welcome h2 i{display:block;width:48px;height:48px;border-radius:50%;background:var(--teal)}
.welcome p{position:absolute;top:132px;left:410px;width:700px;text-align:center;font-size:15px;line-height:24px;color:var(--ink)}

/* levels */
.levels{top:1051px;height:471px;background:linear-gradient(180deg,#3b3b3b,#2a2a2a)}
.levels h2{position:absolute;top:58px;width:100%;text-align:center;font-family:var(--serif);font-weight:400;font-size:52px;color:var(--orange)}
.level-btn{top:152px;width:313px;height:60px;color:var(--white);font-size:24px;display:flex;align-items:center;justify-content:center;letter-spacing:.5px}
.braces{top:0;left:0}
.dot{width:80px;height:80px;border-radius:50%;color:var(--white);font-size:28px;font-weight:500;display:flex;align-items:center;justify-content:center;top:327px;border:3px solid rgba(255,255,255,.2)}
.notch{top:1522px;left:570px;width:0;height:0;border-left:30px solid transparent;border-right:30px solid transparent;border-top:20px solid #2a2a2a;z-index:2}

/* tutor */
.tutor{top:1522px;height:314px;background:var(--white)}
.tutor h2{position:absolute;top:58px;left:94px;font-family:var(--serif);font-weight:400;color:var(--orange);font-size:48px}
.tutor p{position:absolute;top:135px;left:80px;width:650px;font-size:14px;line-height:22px;color:#555}
.tutor-photo{left:802px;top:36px;width:228px;height:228px;border-radius:50%;border:6px solid var(--orange);background:linear-gradient(180deg,#e8d6b9 0%,#c9a77a 55%,#f2f2f2 100%)}

/* talkspan */
.online{top:1836px;height:254px;background:var(--orange);text-align:center}
.online h2{position:absolute;top:70px;left:0;width:100%;font-family:var(--serif);font-weight:400;font-size:54px;color:var(--ink);display:flex;justify-content:center;align-items:center;gap:22px}
.online h2 i{display:block;width:58px;height:58px;border-radius:50%;background:#1e1e1e}
.online p{position:absolute;top:162px;left:330px;width:540px;font-size:15px;line-height:22px;color:var(--white)}

/* book band */
.book{top:2090px;height:268px;background:linear-gradient(90deg,#1f1f1f,#3a3a3a 60%,#262626)}
.book-person{left:100px;top:5px;width:230px;height:263px;background:linear-gradient(180deg,#3b2a20 0%,#2f8bc7 35%,#6a7a8a 70%,#9a7a5a 100%);border-radius:110px 110px 20px 20px;opacity:.9}
.book p{position:absolute;top:78px;left:410px;width:560px;text-align:center;font-family:var(--serif);font-size:30px;line-height:40px;color:var(--white)}
.book-btn{top:157px;left:463px;width:272px;height:66px;background:var(--orange);color:var(--white);font-size:26px;display:flex;align-items:center;justify-content:center;letter-spacing:.5px}

/* why */
.why{top:2358px;height:463px;background:linear-gradient(180deg,#ffffff,#f7f7f7)}
.why h2{position:absolute;top:80px;left:80px;font-family:var(--serif);font-weight:400;color:var(--orange);font-size:52px}
.why ul{position:absolute;top:182px;left:100px;font-size:14px;line-height:24px;color:var(--ink)}
.why p{position:absolute;top:292px;left:80px;width:750px;font-size:14px;line-height:22px;color:var(--ink)}
.why .sign{top:384px;left:80px;color:var(--orange);font-size:16px}
.why-person{left:835px;top:50px;width:300px;height:330px;background:linear-gradient(180deg,#2b1c16 0%,#e9e9e9 35%,#3c4a6a 80%,#f3f3f3 100%);border-radius:140px 140px 40px 40px;opacity:.9}

/* services */
.services{top:2821px;height:343px;background:linear-gradient(135deg,#4d4d4d,#2b2b2b 55%,#1c1c1c)}
.services h2{position:absolute;top:52px;width:100%;text-align:center;font-family:var(--serif);font-weight:400;font-size:52px;color:var(--white)}
.service{top:150px;width:200px;text-align:center;color:var(--white);font-size:16px}
.service .box{width:104px;height:104px;margin:0 auto 16px;border:2px solid rgba(255,255,255,.7);border-radius:8px;display:flex;align-items:center;justify-content:center;background:rgba(0,0,0,.35)}

/* faq */
.faq{top:3164px;height:388px;background:var(--orange)}
.faq h2{position:absolute;top:55px;left:0;width:100%;font-family:var(--serif);font-weight:400;font-size:54px;color:var(--ink);display:flex;justify-content:center;align-items:center;gap:20px}
.faq-badge{display:block;width:90px;height:64px;border-radius:32px;background:#262626;color:var(--orange);font-family:var(--sans);font-size:26px;font-weight:700;line-height:64px;text-align:center}
.faq-list{top:188px;left:209px;width:776px}
.faq-item{height:45px;border:1px solid rgba(255,255,255,.8);margin-bottom:13px;color:var(--white);font-size:14px;display:flex;align-items:center;justify-content:space-between;padding:0 20px}
.faq-item span{width:0;height:0;border-left:8px solid transparent;border-right:8px solid transparent;border-top:10px solid var(--white)}

/* donate */
.donate{top:3552px;height:299px;background:linear-gradient(90deg,#2b2b2b,#3e3e3e 60%,#2b2b2b)}
.donate h2{position:absolute;top:50px;width:100%;text-align:center;font-family:var(--serif);font-weight:400;font-size:48px;color:var(--orange)}
.donate p{position:absolute;top:127px;left:80px;width:590px;font-size:18px;line-height:28px;color:var(--white)}
.donate .divider{top:120px;left:738px;width:2px;height:120px;background:rgba(255,255,255,.5)}
.donate-label{top:132px;left:772px;color:var(--white);font-size:34px;line-height:42px;text-align:center}
.donate-label b{color:var(--orange);font-weight:400}
.donate-art{top:95px;left:960px;width:170px;height:140px;background:linear-gradient(135deg,#6fb544,#2f8f6a);border-radius:70px 20px 70px 20px;opacity:.9}

/* contact */
.contact{top:3851px;height:373px;background:#fafafa}
.contact-person{left:40px;top:20px;width:340px;height:353px;background:linear-gradient(180deg,#3b271d 0%,#e7c8a8 30%,#d0d0d0 65%,#555 100%);border-radius:160px 160px 0 0;opacity:.9}
.contact h2{position:absolute;top:55px;left:700px;font-family:var(--serif);font-weight:400;font-size:52px;color:var(--orange)}
.contact p{position:absolute;top:135px;left:530px;width:560px;text-align:center;font-size:14px;line-height:22px;color:var(--ink)}
.contact-line{top:228px;display:flex;align-items:center;gap:12px;font-size:14px;color:var(--ink)}
.pay{top:302px;left:600px;display:flex;gap:16px}
.pay span{font-family:var(--sans);font-weight:500;font-size:20px;color:var(--ink);background:var(--white);border:1px solid #ddd;padding:6px 14px}

/* footer */
.footer{top:4224px;height:254px;background:#262626;text-align:center}
.to-top{top:18px;left:575px;width:50px;height:50px;border-radius:50%;background:var(--orange);display:flex;align-items:center;justify-content:center}
.footer .brand{top:108px;left:512px}
.footer .brand b{font-size:42px}
.footer .copy{top:198px;width:100%;font-size:13px;color:var(--grey)}
</style>
</head>
<body>

<header class="section hero">
  <div class="photo hero-photo" role="img" aria-label="Photo background of stone steps outdoors"></div>
  <div class="photo hero-person" role="img" aria-label="Photo of a student sitting on steps with a laptop"></div>
  <div class="abs social"><span class="on">chatterloom</span><span>linkora</span><span>glimra</span></div>
  <div class="abs flag" role="img" aria-label="English language flag"></div>
  <div class="abs brand"><i></i><div><b>KiLa</b><small>Solvander learning</small></div></div>
  <nav class="abs nav">
    <a class="active">Home</a><a>About Us</a><a>Why Choose Us?</a><a>Services</a><a>Contact Us</a>
  </nav>
  <div class="abs login">Login</div>
  <h1 class="abs hero-title">Online learning,<br>nrwegian studies</h1>
  <p class="abs hero-sub">sarn, emt, approved by emt, approved by sarn, norwegian course, study online etc.</p>
  <div class="abs arrows"><span>&laquo;</span><span>&raquo;</span></div>
</header>

<section class="section welcome">
  <div class="photo welcome-photo" role="img" aria-label="Portrait photo of the teacher"></div>
  <h2>Welcome To KiLa <i></i></h2>
  <p>KiLa is an online school offering custom made courses for everyone who want to learn Norwegian. Whether you are living abroad or in Norway, you can learn Norwegian with the online programs. You will also speak to your tutor in talkspan, as part of the course. KiLa is approved by SARN and EMT, and all hours will be credited and counted as part of the mandatory 250 hours or 550 hours Norwegian as well as 50 hours social studies.</p>
</section>

<section class="section levels">
  <h2>KiLa offers all levels of Norwegian</h2>
  <div class="abs level-btn" style="left:75px;background:var(--teal)">BASIC USER</div>
  <div class="abs level-btn" style="left:442px;background:var(--orange)">INDEPENDENT USER</div>
  <div class="abs level-btn" style="left:809px;background:var(--magenta)">PROFICIENT USER</div>
  <svg class="abs braces" width="1200" height="471" viewBox="0 0 1200 471" fill="none" stroke="#ffffff" stroke-width="5" stroke-linecap="round">
    <path d="M119 320 Q119 275 160 275 L205 275 Q234 275 234 250 Q234 275 263 275 L308 275 Q349 275 349 320"/>
    <path d="M484 320 Q484 275 525 275 L568 275 Q597 275 597 250 Q597 275 626 275 L670 275 Q711 275 711 320"/>
    <path d="M851 320 Q851 275 892 275 L937 275 Q966 275 966 250 Q966 275 995 275 L1040 275 Q1081 275 1081 320"/>
  </svg>
  <div class="abs dot" style="left:79px;background:var(--green)">A1</div>
  <div class="abs dot" style="left:309px;background:var(--teal-light)">A2</div>
  <div class="abs dot" style="left:444px;background:var(--teal-light)">B1</div>
  <div class="abs dot" style="left:671px;background:var(--teal-light)">B2</div>
  <div class="abs dot" style="left:811px;background:var(--teal-light)">C1</div>
  <div class="abs dot" style="left:1041px;background:var(--teal-light)">C2</div>
</section>
<div class="abs notch"></div>

<section class="section tutor">
  <h2>Maren Holtvik</h2>
  <p>I am educated a teacher from Fjordvik University College, and I have been teaching Norwegian as a second language for more than 10 years. I have lived abroad in North Canada and Tanzania and I would say I have an international mindset. As a teacher, I am energetic and passionate about my work, and I think that learning the language in the country where you live is the key to success.</p>
  <div class="photo tutor-photo" role="img" aria-label="Portrait photo of the tutor"></div>
</section>

<section class="section online">
  <h2>Online tutoring in talkspan <i></i></h2>
  <p>Online tutoring is a great opportunity to learn Norwegian from your own livingroom! All lessons are customized to your needs.</p>
</section>

<section class="section book">
  <div class="photo book-person" role="img" aria-label="Photo of a young man sitting with a laptop"></div>
  <p>Lorem Ipsum is simply dummy text of the printing and typesetting industry.</p>
  <div class="abs book-btn">BOOK A COURSE</div>
</section>

<section class="section why">
  <h2>Why Choose KiLa</h2>
  <ul>
    <li>Approved by SARN and EMT</li>
    <li>Best prices on online courses</li>
    <li>Simple, easy and efficient</li>
    <li>Learn from your own home, office or even when you are travelling</li>
  </ul>
  <p>At KiLa I strive to provide high quality lessons in Norwegian language. KiLa aims to make sure each and every student gains new skills and achieves something by the end of each personally customized lesson in Norwegian. I aspire to make sure all our students are satisfied with all my services.</p>
  <div class="abs sign">- Best wishes, Maren</div>
  <div class="photo why-person" role="img" aria-label="Photo of a woman sitting cross-legged with a laptop"></div>
</section>

<section class="section services">
  <h2>Our Services</h2>
  <div class="abs service" style="left:154px">
    <div class="box"><svg width="50" height="62" viewBox="0 0 50 62" fill="none" stroke="#fff" stroke-width="3"><rect x="4" y="3" width="42" height="56" rx="5"/><line x1="4" y1="48" x2="46" y2="48"/><circle cx="25" cy="54" r="2" fill="#fff"/></svg></div>
    Norskkurs online
  </div>
  <div class="abs service" style="left:497px">
    <div class="box"><svg width="62" height="56" viewBox="0 0 62 56" fill="none" stroke="#fff" stroke-width="3"><circle cx="22" cy="18" r="9"/><path d="M6 52 Q6 32 22 32 Q38 32 38 52Z"/><circle cx="44" cy="14" r="7"/><path d="M40 28 Q56 26 58 44"/></svg></div>
    Social Studies 50 hours
  </div>
  <div class="abs service" style="left:855px">
    <div class="box"><svg width="52" height="62" viewBox="0 0 52 62" fill="none" stroke="#fff" stroke-width="3"><path d="M6 3 H34 L46 15 V59 H6Z"/><line x1="14" y1="24" x2="38" y2="24"/><line x1="14" y1="34" x2="38" y2="34"/><line x1="14" y1="44" x2="30" y2="44"/></svg></div>
    Feedback on written<br>assignments
  </div>
</section>

<section class="section faq">
  <h2>Fequently Ask Questions <span class="faq-badge">FAQ</span></h2>
  <div class="abs faq-list">
    <div class="faq-item">Do you offer private or group classes?<span></span></div>
    <div class="faq-item">Where are most of your students from?<span></span></div>
    <div class="faq-item">What type of people study Norwegian at KiLa?<span></span></div>
  </div>
</section>

<section class="section donate">
  <h2>Donations to voluntary work</h2>
  <p>Lorem Ipsum is simply dummy text of the printing and type setting industry. Lorem Ipsum has been the industry's standard dummy text ever since the 1500s.</p>
  <div class="abs divider"></div>
  <div class="abs donate-label">Donate to<br><b>KILA</b></div>
  <div class="abs donate-art" role="img" aria-label="Illustration of an open hand holding a symbol"></div>
</section>

<section class="section contact">
  <div class="photo contact-person" role="img" aria-label="Photo of a smiling customer service woman with a headset"></div>
  <h2>Contact Us</h2>
  <p>Are you interested in learning Norwegian or take the social studies course online? Please send me a message today and I will get in touch with you.</p>
  <div class="abs contact-line" style="left:585px">
    <svg width="26" height="26" viewBox="0 0 24 24" fill="#555"><path d="M6.6 10.8a15 15 0 0 0 6.6 6.6l2.2-2.2c.3-.3.7-.4 1-.2 1.1.4 2.3.6 3.6.6.6 0 1 .4 1 1V20c0 .6-.4 1-1 1A17 17 0 0 1 3 4c0-.6.4-1 1-1h3.5c.6 0 1 .4 1 1 0 1.3.2 2.5.6 3.6.1.3 0 .7-.2 1z"/></svg>
    +47 400 12 345
  </div>
  <div class="abs contact-line" style="left:785px">
    <svg width="28" height="20" viewBox="0 0 28 20" fill="none" stroke="#555" stroke-width="2"><rect x="1" y="1" width="26" height="18"/><path d="M1 1 L14 11 L27 1"/></svg>
    maren@solvanderlearn.com
  </div>
  <div class="abs pay"><span>Corda</span><span>Bluvex</span><span>Coinlyx</span><span>Frensa</span></div>
</section>

<footer class="section footer">
  <div class="abs to-top"><svg width="20" height="14" viewBox="0 0 20 14"><path d="M10 0 L20 14 H0Z" fill="#262626"/></svg></div>
  <div class="abs brand"><i></i><div><b>KiLa</b><small>Solvander learning</small></div></div>
  <div class="abs copy">© KiLa - 2015. All Rights Reserved.</div>
</footer>

</body>
</html>
```